Design for new site

Hi, we need a web design for a new product calmridgeway.
This product is aimed to help people with anxiety, panic attacks and other disorders on permanently basis.
Please take a look at competitors web-sites:
http://www.brightharborpath.example/
http://www.stillmeadow.example/
Key Audiences
The intended audience for this site will be people that are looking for relief from panic and anxiety.
Key Objectives
Key object is to get prospective clients to sign up for membership and purchase our audio course.
Theme of Site
The general site theme needs to be clean and simple. The audience coming to the site in under a lot of anxiety and we don’t want to add any stress.
The site needs to flow easy from top down, with few distractions in side menus and/or columns.
Color Scheme
Suggested colors need to be light shades of blue. Blue psychology is tranquil, peaceful, and calm. This color has a tremendous stress management quality to it, making us feel cool and calm.
Or it can be shades of cool green of summer forest.
Please take a look at site mock up in attachment.

```html
<!DOCTYPE html>
<html lang="en">
<head>
<meta charset="utf-8">
<title>Calmridgeway – Relief from panic and anxiety</title>
<link href="https://fonts.googleapis.com/css2?family=Open+Sans:wght@400;600;700&family=Roboto+Condensed:wght@400;700&display=swap" rel="stylesheet">
<style>
  :root{
    --brand:#1e8fc0;
    --teal:#27a3c8;
    --teal-light:#3fb3d4;
    --teal-pale:#d9eff6;
    --navy:#13284a;
    --ink:#2c3a4a;
    --muted:#6b7884;
    --line:#d6dde3;
    --white:#ffffff;
    --hero-dark:#2d3238;
    --hero-mid:#566470;
  }
  *{box-sizing:border-box;margin:0;padding:0}
  html,body{width:769px;height:1200px;overflow:hidden}
  body{position:relative;background:var(--white);font-family:"Open Sans",Arial,sans-serif;color:var(--ink);font-size:9px;line-height:1.45}
  .abs{position:absolute}
  .heading{font-family:"Roboto Condensed","Arial Narrow",sans-serif;font-weight:700;color:var(--navy)}

  /* header */
  .site-header{left:0;top:0;width:769px;height:76px;background:var(--white)}
  .logo{left:0;width:769px;top:18px;text-align:center;font-family:"Roboto Condensed","Arial Narrow",sans-serif;font-weight:700;font-size:38px;letter-spacing:1px;color:var(--brand)}
  .social-top{right:16px;top:8px;display:flex;gap:5px}
  .dot{width:15px;height:15px;border-radius:50%;background:var(--teal)}

  /* hero */
  .hero{left:0;top:76px;width:769px;height:242px;overflow:hidden}
  .hero-art{left:0;top:0;width:769px;height:242px;background:linear-gradient(180deg,#1f2327 0%,var(--hero-mid) 50%,var(--hero-dark) 100%)}
  .aim-bubble{left:572px;top:30px;width:150px;height:150px;border-radius:50%;background:var(--white);display:flex;align-items:center;justify-content:center;text-align:center;padding:22px;font-size:12.5px;line-height:1.3;color:var(--navy)}

  /* sign up panel */
  .signup{left:140px;top:318px;width:490px;height:250px;background:var(--white);box-shadow:0 2px 8px rgba(0,0,0,.18)}
  .signup-tab{left:252px;top:0;width:238px;height:22px;background:var(--teal);color:var(--white);font-weight:700;font-size:10.5px;padding:4px 12px}
  .video{left:12px;top:36px;width:228px;height:148px;background:var(--teal)}
  .play{left:88px;top:48px;width:52px;height:52px}
  .form{left:256px;top:34px;width:222px}
  .form-title{font-family:"Roboto Condensed","Arial Narrow",sans-serif;font-weight:700;font-size:20px;color:var(--navy);text-align:center;border-bottom:2px solid var(--teal);padding-bottom:3px;margin-bottom:12px}
  .field{display:flex;align-items:center;margin:0 0 8px 18px;font-size:8.5px;color:var(--muted)}
  .field span{width:54px}
  .field i{display:block;width:120px;height:16px;border:1px solid var(--line);background:#f7f9fa}
  .btn{display:block;background:var(--teal);color:var(--white);font-weight:700;font-size:10px;text-align:center;border-radius:3px;padding:5px 0}
  .form .btn{margin:12px 20px 0 40px}
  .social-row{left:320px;top:202px;display:flex;gap:6px}
  .social-row .dot{width:17px;height:17px}

  /* features */
  .section-title{left:0;width:769px;text-align:center;font-size:22px}
  .features{left:120px;top:614px;width:530px;display:flex;justify-content:space-between}
  .feature{width:160px;text-align:center}
  .feature-icon{width:50px;height:50px;border-radius:50%;background:var(--teal);margin:0 auto 8px;display:flex;align-items:center;justify-content:center}
  .feature h3{font-family:"Roboto Condensed","Arial Narrow",sans-serif;font-size:13px;color:var(--navy);margin-bottom:3px}
  .feature p{font-size:8px;color:var(--muted)}
  .feature a{color:var(--teal);font-weight:600;text-decoration:none}
  .feature ul{list-style:none;text-align:left;display:inline-block;font-size:8px;line-height:1.4;color:var(--muted)}
  .feature li::before{content:"• ";color:var(--teal)}

  /* about */
  .about{left:0;top:755px;width:769px;height:140px;background:var(--teal-light);color:var(--white)}
  .about h2{text-align:center;font-family:"Roboto Condensed","Arial Narrow",sans-serif;font-size:22px;margin:14px 0 10px}
  .about-box{margin:0 auto;width:480px;background:rgba(255,255,255,.12);padding:8px 12px;font-size:8.5px}
  .about-box p+p{margin-top:6px}

  /* secret + testimonials */
  .col-title{font-size:15px;text-align:center;border-bottom:1px solid var(--line);padding-bottom:5px;margin-bottom:10px}
  .secret{left:140px;top:910px;width:240px}
  .bubble{background:var(--teal);color:var(--white);font-size:8px;border-radius:6px;padding:5px 9px;margin-bottom:7px;position:relative}
  .bubble::after{content:"";position:absolute;left:14px;bottom:-5px;border:5px solid transparent;border-top-color:var(--teal);border-bottom:0}
  .secret p{font-size:8.5px;color:var(--ink);margin-top:4px}
  .secret .sign{color:var(--teal);font-weight:700;margin-top:6px}
  .testimonials{left:400px;top:910px;width:230px}
  .quote{display:flex;gap:10px;margin-bottom:14px}
  .avatar{flex:none;width:44px;height:44px;border-radius:50%;background:linear-gradient(135deg,#c9b6a4,#8c9aa6)}
  .quote p{font-size:8px;color:var(--muted)}
  .quote b{display:block;color:var(--teal);font-size:8.5px;margin-top:3px}

  /* bottom strip + footer */
  .cta-strip{left:0;top:1120px;width:769px;height:30px;background:var(--teal-pale);display:flex;align-items:center;justify-content:center;gap:26px}
  .cta-strip .heading{font-size:15px}
  .cta-strip .btn{background:var(--navy);padding:4px 12px;font-size:9px}
  .footer{left:0;top:1150px;width:769px;height:50px;background:var(--navy);color:var(--white)}
  .footer-social{left:140px;top:8px;display:flex;gap:5px}
  .footer-social .dot{background:#2c4670}
  .footer-links{left:140px;top:30px;font-size:7.5px;font-weight:600}
  .footer-logo{left:470px;top:6px;font-family:"Roboto Condensed","Arial Narrow",sans-serif;font-weight:700;font-size:20px;color:var(--brand)}
  .copyright{left:520px;top:32px;font-size:7px;color:#b9c3d1}
</style>
</head>
<body>

<header class="abs site-header">
  <div class="abs logo">CALMRIDGEWAY</div>
  <div class="abs social-top"><span class="dot"></span><span class="dot"></span><span class="dot"></span><span class="dot"></span><span class="dot"></span><span class="dot"></span></div>
</header>

<section class="abs hero">
  <div class="abs hero-art" role="img" aria-label="Hero illustration: a head made of a glowing maze rising over a stormy city landscape"></div>
  <div class="abs aim-bubble">Our aimed to help people with anxiety, panic attacks and other disorders on permanently basis.</div>
</section>

<section class="abs signup">
  <div class="abs signup-tab">Sign up for membership</div>
  <div class="abs video" role="img" aria-label="Introductory video">
    <svg class="abs play" viewBox="0 0 52 52"><rect width="52" height="52" rx="10" fill="#0f6f90"/><path d="M20 15 L38 26 L20 37 Z" fill="#ffffff"/></svg>
  </div>
  <form class="abs form">
    <div class="form-title">Calmridgeway NOW!</div>
    <div class="field"><span>First Name:</span><i></i></div>
    <div class="field"><span>Last Name:</span><i></i></div>
    <div class="field"><span>Email:</span><i></i></div>
    <span class="btn">Get FREE Calmridgeway</span>
  </form>
  <div class="abs social-row"><span class="dot"></span><span class="dot"></span><span class="dot"></span><span class="dot"></span><span class="dot"></span><span class="dot"></span><span class="dot"></span></div>
</section>

<h2 class="abs heading section-title" style="top:578px">Looking for relief from panic and anxiety?</h2>

<section class="abs features">
  <div class="feature">
    <div class="feature-icon"><svg width="28" height="24" viewBox="0 0 30 26"><rect x="1" y="1" width="28" height="18" rx="2" fill="none" stroke="#fff" stroke-width="2"/><rect x="11" y="21" width="8" height="4" fill="#fff"/></svg></div>
    <h3>Webinars</h3>
    <p>Join our free live sessions and learn calm breathing steps you can use at home every day. <a>Read more</a></p>
  </div>
  <div class="feature">
    <div class="feature-icon"><svg width="28" height="24" viewBox="0 0 30 26"><path d="M3 2h18a2 2 0 0 1 2 2v10a2 2 0 0 1-2 2H10l-5 4v-4H3a2 2 0 0 1-2-2V4a2 2 0 0 1 2-2z" fill="#fff"/><path d="M25 8h2a2 2 0 0 1 2 2v9a2 2 0 0 1-2 2h-1v4l-5-4h-7" fill="none" stroke="#fff" stroke-width="2"/></svg></div>
    <h3>FREE Calmridgeway</h3>
    <p>Sign up today to get the first part of the audio course and start feeling lighter now. <a>Read more</a></p>
  </div>
  <div class="feature">
    <div class="feature-icon"><svg width="24" height="26" viewBox="0 0 26 28"><path d="M13 2v16M6 11l7 7 7-7" fill="none" stroke="#fff" stroke-width="3"/><path d="M2 21v5h22v-5" fill="none" stroke="#fff" stroke-width="3"/></svg></div>
    <h3>Free Downloads</h3>
    <ul><li>Calm Breathing Guide</li><li>Short Relaxation Audio</li><li>Daily Anxiety Journal</li><li>Sleep Routine Plan</li></ul>
  </div>
</section>

<section class="abs about">
  <h2>About Us</h2>
  <div class="about-box">
    <p>We started this program to give people a simple, gentle path out of panic and worry. Our audio lessons guide you step by step, at your own pace, in your own home, with no pressure and no rush at all.</p>
    <p>Thousands of members have used these calm methods to quiet racing thoughts, sleep better and return to the everyday life they missed.</p>
  </div>
</section>

<section class="abs secret">
  <h2 class="heading col-title">What's our secret?</h2>
  <div class="bubble">We teach one small calming habit at a time so it sticks.</div>
  <div class="bubble">Every lesson is short, clear and easy to follow daily.</div>
  <div class="bubble">Our methods work with your body, not against it.</div>
  <p>Try it for yourself and get the first lessons of the course free today with simple sign up.</p>
  <p class="sign">The Team</p>
</section>

<section class="abs testimonials">
  <h2 class="heading col-title">Testimonials</h2>
  <div class="quote">
    <div class="avatar" role="img" aria-label="Portrait photo of a member"></div>
    <p>“The lessons helped me breathe through hard moments and feel calm again at work.”<b>Mara Lind</b></p>
  </div>
  <div class="quote">
    <div class="avatar" role="img" aria-label="Portrait photo of a member"></div>
    <p>“After a few weeks I slept well and stopped fearing the next attack.”<b>Owen Pryce</b></p>
  </div>
</section>

<div class="abs cta-strip">
  <span class="heading">Looking for relief from panic and anxiety?</span>
  <span class="btn">Get FREE Calmridgeway</span>
</div>

<footer class="abs footer">
  <div class="abs footer-social"><span class="dot"></span><span class="dot"></span><span class="dot"></span><span class="dot"></span><span class="dot"></span><span class="dot"></span></div>
  <div class="abs footer-links">Privacy Policy &nbsp;|&nbsp; Refund Policy &nbsp;|&nbsp; Terms of Service</div>
  <div class="abs footer-logo">CALMRIDGEWAY</div>
  <div class="abs copyright">Copyright © 2014</div>
</footer>

</body>
</html>
```